Figure for a research paper

I am working on designing a figure for a research paper that illustrates the effect of KORA Pathway assessment on student outcomes over time by impacting teacher bias and teacher perception of student growth. I built the attached figure via powerpoint. It includes the very basic elements but it does not look great and I am not sure that it is clearly depicting what I am hoping to illustrate. I would like for you to build an illustration of this idea that i can include in the paper.

```html
<!DOCTYPE html>
<html lang="en">
<head>
<meta charset="utf-8">
<title>Effect of KORA Pathway Assessment on SEL Program Effectiveness Over Time</title>
<link rel="stylesheet" href="https://fonts.googleapis.com/css2?family=Roboto:wght@700&display=swap">
<style>
  :root {
    --ink: #176183;
    --trend: #ff0000;
    --paper: #ffffff;
  }
  html, body {
    margin: 0;
    padding: 0;
    width: 1200px;
    height: 1200px;
    overflow: hidden;
    background: var(--paper);
  }
  .figure {
    display: block;
    width: 1200px;
    height: 1200px;
  }
  .figure text {
    font-family: "Roboto", Arial, sans-serif;
    font-weight: 700;
    fill: var(--ink);
  }
  .axis { fill: var(--ink); }
  .trend-line { stroke: var(--trend); stroke-width: 5; }
  .callout-frame { fill: var(--paper); stroke: var(--ink); stroke-width: 2.5; }
  .arrow { fill: var(--ink); }
  .figure-slot { fill: var(--ink); }
  .axis-label-y { font-size: 23.5px; }
  .axis-label-x { font-size: 46px; }
  .callout-bias { font-size: 21px; }
  .callout-perception { font-size: 14px; }
  .callout-assessment { font-size: 23px; }
  .clock-face { fill: none; stroke: var(--ink); stroke-width: 4.5; }
  .clock-hand { stroke: var(--ink); stroke-width: 2; stroke-linecap: round; }
</style>
</head>
<body>
<svg class="figure" viewBox="0 0 1200 1200" xmlns="http://www.w3.org/2000/svg">

  <!-- Axes -->
  <rect class="axis axis-y" x="326" y="361" width="20" height="453"/>
  <rect class="axis axis-x" x="287" y="755" width="784" height="19"/>

  <!-- Growth trend -->
  <line class="trend-line" x1="346" y1="754" x2="1071" y2="436"/>

  <!-- Y axis label -->
  <rect class="figure-slot" x="185" y="453" width="83" height="96" rx="10"
        role="img" aria-label="Silhouettes of two students standing side by side"/>
  <text class="axis-label-y" text-anchor="middle">
    <tspan x="226" y="570">Effectiveness</tspan>
    <tspan x="226" y="597">of SEL Program</tspan>
    <tspan x="226" y="624">on the student</tspan>
  </text>

  <!-- Callout: teacher bias -->
  <g class="callout callout-bias-group">
    <rect class="arrow" x="491" y="454" width="16" height="118"/>
    <polygon class="arrow" points="482,571 516,571 499,600"/>
    <rect class="callout-frame" x="425" y="375" width="162" height="79"/>
    <text class="callout-bias" text-anchor="middle">
      <tspan x="481" y="406">Teacher</tspan>
      <tspan x="481" y="429">Bias</tspan>
    </text>
    <rect class="figure-slot" x="558" y="398" width="37" height="97" rx="6"
          role="img" aria-label="Silhouette of a teacher holding a pointer and a book"/>
  </g>

  <!-- Callout: inaccurate perception -->
  <g class="callout callout-perception-group">
    <rect class="arrow" x="783" y="455" width="17" height="30"/>
    <polygon class="arrow" points="774,485 809,485 791,513"/>
    <rect class="callout-frame" x="712" y="376" width="164" height="79"/>
    <text class="callout-perception" text-anchor="middle">
      <tspan x="781" y="397">Teacher inaccurate</tspan>
      <tspan x="781" y="412">perception</tspan>
      <tspan x="781" y="427">of student growth</tspan>
      <tspan x="781" y="442">or learning</tspan>
    </text>
    <rect class="figure-slot" x="851" y="398" width="38" height="97" rx="6"
          role="img" aria-label="Silhouette of a teacher holding a pointer and a book"/>
  </g>

  <!-- Callout: assessment lifting the trend -->
  <g class="callout callout-assessment-group">
    <rect class="arrow" x="678" y="640" width="13" height="21"/>
    <polygon class="arrow" points="672,641 697,641 684,621"/>
    <rect class="arrow" x="868" y="640" width="13" height="21"/>
    <polygon class="arrow" points="862,641 887,641 874,621"/>
    <rect class="callout-frame" x="607" y="660" width="344" height="45"/>
    <text class="callout-assessment" x="779" y="691" text-anchor="middle">KORA Pathway Assessment</text>
  </g>

  <!-- X axis label -->
  <g class="time-label">
    <circle class="clock-face" cx="666" cy="814" r="31"/>
    <line class="clock-hand" x1="666" y1="814" x2="664" y2="795"/>
    <line class="clock-hand" x1="666" y1="814" x2="686" y2="829"/>
    <circle class="arrow" cx="666" cy="814" r="4"/>
    <text class="axis-label-x" x="706" y="830">Time</text>
  </g>

</svg>
</body>
</html>
```